ReDesign CBD Packaging Box with needed Details and Pizazzz!

I have 3 things that need to be accomplished for this project to be completed.
1- Each box contains CBD oil in values of 500mg, 1500mg and 2500mg. Each value as a flavor as well. We offer 4 "Flavors": Natural (flavorless), Mint, Dragonfruit and Watermelon in the 3 variants listed above. So need a box for each.
2- After reviewing the design recently, I decided I am not as happy as I thought. So, I am open to any modifications that may make is shine and spark that says "buy me" figuratively.
3- The box should be easy to identify in terms of the amount of CBD and flavor it is. Play with colors maybe where the swirl is white is it is 2500mg, and gray if 1500mg and dark gray for 500mg? Something like that as an example but I am sure you have better ideas than I .

So to summarize, need to update the box with all the wording and information required to be on the box.

I am attaching:
1)the text that should be on the box in case you need it
2) the logo,
3)a version that i tried to making called "dragon fruit tincture 1500mg",
4)the original design packaging called "soapy packaging".
5)the template I am supposed to use.

Target Market(s)

Health and Nutrition, Sports, Alternative Medicine, Elderly,

Industry/Entity Type

Retail online

Requirements
Must have
• clear writing with clear font
Nice to have
• some color or absence of black maybe.
Should not have
• unnecessary images or too busy

```html
<!DOCTYPE html>
<html lang="en">
<head>
<meta charset="utf-8">
<title>Lathera CBD Tincture Packaging</title>
<link rel="stylesheet" href="https://fonts.googleapis.com/css2?family=Oswald:wght@400;500;600;700&family=Yellowtail&family=Josefin+Sans:wght@400;600&display=swap">
<style>
  :root {
    --bg-top: #ececec;
    --bg-bottom: #9d9d9d;
    --white: #ffffff;
    --grey-text: #9a9a9a;
    --grey-pill: #a9a9a9;
    --badge-ring: #b9b9b9;
    --gold-dark: #b88a2c;
    --gold-light: #f6e6a4;
    --dragon: #a82760;
    --dragon-soft: #cb79a0;
    --melon: #c1343c;
    --melon-soft: #dc8789;
    --mint: #256b2f;
    --mint-soft: #80a986;
    --natural: #78bf31;
    --natural-soft: #acd883;
  }
  * { box-sizing: border-box; margin: 0; padding: 0; }
  html, body { width: 1200px; height: 821px; overflow: hidden; }
  body {
    background: linear-gradient(180deg, var(--bg-top) 0%, var(--bg-bottom) 100%);
    font-family: "Oswald", sans-serif;
    position: relative;
  }
  .box-lineup {
    position: absolute;
    top: 116px;
    left: 182px;
    display: flex;
    gap: 25px;
  }
  .box-front {
    width: 190px;
    height: 553px;
    background: var(--white);
    display: flex;
    flex-direction: column;
    box-shadow: 0 6px 14px rgba(0,0,0,0.18);
  }
  .box-front--dragonfruit { --flavor: var(--dragon); --flavor-soft: var(--dragon-soft); --accent: var(--dragon); }
  .box-front--watermelon { --flavor: var(--melon); --flavor-soft: var(--melon-soft); --accent: var(--melon); }
  .box-front--mint { --flavor: var(--mint); --flavor-soft: var(--mint-soft); --accent: var(--mint); }
  .box-front--natural { --flavor: var(--natural); --flavor-soft: var(--natural-soft); --accent: var(--natural); }

  .lid {
    height: 24px;
    display: flex;
    align-items: center;
    justify-content: center;
    font-size: 14px;
    font-weight: 500;
    letter-spacing: 1px;
    color: #d3d3d3;
  }
  .flavor-panel {
    height: 323px;
    background: var(--flavor);
    position: relative;
    display: flex;
    flex-direction: column;
    align-items: center;
  }
  .brand-name {
    margin-top: 40px;
    font-size: 30px;
    font-weight: 500;
    letter-spacing: 1px;
    color: var(--white);
    line-height: 1;
  }
  .flavor-art {
    position: absolute;
    top: 122px;
    left: 15px;
    width: 160px;
    height: 178px;
  }
  .flavor-name {
    position: absolute;
    bottom: 4px;
    width: 100%;
    text-align: center;
    font-size: 27px;
    font-weight: 600;
    color: var(--white);
    line-height: 1.1;
  }
  .spectrum-band {
    height: 30px;
    background: linear-gradient(90deg, var(--gold-dark) 0%, var(--gold-light) 50%, var(--gold-dark) 100%);
    display: flex;
    align-items: center;
    justify-content: center;
    font-family: "Yellowtail", cursive;
    font-size: 24px;
    color: var(--white);
    padding-top: 2px;
  }
  .product-info {
    flex: 1;
    display: flex;
    flex-direction: column;
    align-items: center;
  }
  .product-type {
    margin-top: 2px;
    font-size: 27px;
    font-weight: 600;
    color: var(--accent);
    line-height: 1.15;
  }
  .strength {
    display: flex;
    align-items: center;
    gap: 3px;
    color: var(--grey-text);
    margin-top: 2px;
  }
  .strength__value { font-size: 24px; font-weight: 600; line-height: 1; }
  .strength__unit {
    font-family: "Josefin Sans", sans-serif;
    font-size: 10px;
    line-height: 0.95;
    margin-right: 6px;
  }
  .badges {
    display: flex;
    gap: 18px;
    margin-top: 14px;
  }
  .badge { width: 44px; height: 44px; }
  .certified-pill {
    margin-top: 6px;
    background: var(--grey-pill);
    color: var(--white);
    font-size: 8.5px;
    font-weight: 500;
    letter-spacing: 0.3px;
    padding: 2px 6px;
    border-radius: 3px;
  }
  .volume {
    margin-top: 12px;
    font-family: "Josefin Sans", sans-serif;
    font-size: 13px;
    color: var(--grey-text);
    letter-spacing: 0.5px;
    word-spacing: 4px;
  }
</style>
</head>
<body>
<main class="box-lineup">

  <article class="box-front box-front--dragonfruit">
    <div class="lid">Lathera</div>
    <section class="flavor-panel">
      <div class="brand-name">Lathera</div>
      <svg class="flavor-art" viewBox="0 0 160 178" role="img" aria-label="Photo of a whole and halved dragonfruit">
        <path d="M80 0 C110 30 160 60 160 98 A80 80 0 0 1 0 98 C0 60 50 30 80 0 Z" fill="var(--flavor-soft)"/>
        <ellipse cx="84" cy="130" rx="56" ry="42" fill="#e3a1bf"/>
      </svg>
      <h2 class="flavor-name">DRAGONFRUIT</h2>
    </section>
    <div class="spectrum-band">Full Spectrum</div>
    <section class="product-info">
      <h3 class="product-type">CBD TINCTURE</h3>
      <div class="strength">
        <span class="strength__value">2500</span><span class="strength__unit">MG<br>CBD</span>
        <span class="strength__value">45</span><span class="strength__unit">MG CBD<br>PER ML</span>
      </div>
      <div class="badges">
        <svg class="badge" viewBox="0 0 44 44" aria-hidden="true"><circle cx="22" cy="22" r="19" fill="none" stroke="var(--badge-ring)" stroke-width="2.5"/></svg>
        <svg class="badge" viewBox="0 0 44 44" aria-hidden="true"><circle cx="22" cy="22" r="19" fill="none" stroke="var(--badge-ring)" stroke-width="2.5"/></svg>
      </div>
      <div class="certified-pill">ALL NATURAL AND VEGAN CERTIFIED</div>
      <div class="volume">2 fl oz. 59.1471 mL</div>
    </section>
  </article>

  <article class="box-front box-front--watermelon">
    <div class="lid">Lathera</div>
    <section class="flavor-panel">
      <div class="brand-name">Lathera</div>
      <svg class="flavor-art" viewBox="0 0 160 178" role="img" aria-label="Photo of watermelon slices">
        <path d="M80 0 C110 30 160 60 160 98 A80 80 0 0 1 0 98 C0 60 50 30 80 0 Z" fill="var(--flavor-soft)"/>
        <ellipse cx="84" cy="125" rx="64" ry="38" fill="#e4676a"/>
      </svg>
      <h2 class="flavor-name">WATERMELON</h2>
    </section>
    <div class="spectrum-band">Full Spectrum</div>
    <section class="product-info">
      <h3 class="product-type">CBD TINCTURE</h3>
      <div class="strength">
        <span class="strength__value">2500</span><span class="strength__unit">MG<br>CBD</span>
        <span class="strength__value">45</span><span class="strength__unit">MG CBD<br>PER ML</span>
      </div>
      <div class="badges">
        <svg class="badge" viewBox="0 0 44 44" aria-hidden="true"><circle cx="22" cy="22" r="19" fill="none" stroke="var(--badge-ring)" stroke-width="2.5"/></svg>
        <svg class="badge" viewBox="0 0 44 44" aria-hidden="true"><circle cx="22" cy="22" r="19" fill="none" stroke="var(--badge-ring)" stroke-width="2.5"/></svg>
      </div>
      <div class="certified-pill">ALL NATURAL AND VEGAN CERTIFIED</div>
      <div class="volume">2 fl oz. 59.1471 mL</div>
    </section>
  </article>

  <article class="box-front box-front--mint">
    <div class="lid">Lathera</div>
    <section class="flavor-panel">
      <div class="brand-name">Lathera</div>
      <svg class="flavor-art" viewBox="0 0 160 178" role="img" aria-label="Photo of mint leaves with purple flowers">
        <path d="M80 0 C110 30 160 60 160 98 A80 80 0 0 1 0 98 C0 60 50 30 80 0 Z" fill="var(--flavor-soft)"/>
        <ellipse cx="82" cy="125" rx="62" ry="46" fill="#4d8a45"/>
      </svg>
      <h2 class="flavor-name">MINT</h2>
    </section>
    <div class="spectrum-band">Full Spectrum</div>
    <section class="product-info">
      <h3 class="product-type">CBD TINCTURE</h3>
      <div class="strength">
        <span class="strength__value">2500</span><span class="strength__unit">MG<br>CBD</span>
        <span class="strength__value">45</span><span class="strength__unit">MG CBD<br>PER ML</span>
      </div>
      <div class="badges">
        <svg class="badge" viewBox="0 0 44 44" aria-hidden="true"><circle cx="22" cy="22" r="19" fill="none" stroke="var(--badge-ring)" stroke-width="2.5"/></svg>
        <svg class="badge" viewBox="0 0 44 44" aria-hidden="true"><circle cx="22" cy="22" r="19" fill="none" stroke="var(--badge-ring)" stroke-width="2.5"/></svg>
      </div>
      <div class="certified-pill">ALL NATURAL AND VEGAN CERTIFIED</div>
      <div class="volume">2 fl oz. 59.1471 mL</div>
    </section>
  </article>

  <article class="box-front box-front--natural">
    <div class="lid">Lathera</div>
    <section class="flavor-panel">
      <div class="brand-name">Lathera</div>
      <svg class="flavor-art" viewBox="0 0 160 178" role="img" aria-label="Photo of a leafy green plant">
        <path d="M80 0 C110 30 160 60 160 98 A80 80 0 0 1 0 98 C0 60 50 30 80 0 Z" fill="var(--flavor-soft)"/>
        <ellipse cx="82" cy="122" rx="66" ry="46" fill="#2f5a3a"/>
      </svg>
      <h2 class="flavor-name">NARURAL</h2>
    </section>
    <div class="spectrum-band">Full Spectrum</div>
    <section class="product-info">
      <h3 class="product-type">CBD TINCTURE</h3>
      <div class="strength">
        <span class="strength__value">2500</span><span class="strength__unit">MG<br>CBD</span>
        <span class="strength__value">45</span><span class="strength__unit">MG CBD<br>PER ML</span>
      </div>
      <div class="badges">
        <svg class="badge" viewBox="0 0 44 44" aria-hidden="true"><circle cx="22" cy="22" r="19" fill="none" stroke="var(--badge-ring)" stroke-width="2.5"/></svg>
        <svg class="badge" viewBox="0 0 44 44" aria-hidden="true"><circle cx="22" cy="22" r="19" fill="none" stroke="var(--badge-ring)" stroke-width="2.5"/></svg>
      </div>
      <div class="certified-pill">ALL NATURAL AND VEGAN CERTIFIED</div>
      <div class="volume">2 fl oz. 59.1471 mL</div>
    </section>
  </article>

</main>
</body>
</html>
```